All stationery items: Business Cards, Letter Heads, and Envelops
Real Estate Business
All stationery items:  Business Cards, Letter Heads, and Envelops  - Real Estate
Creative Brief
Simple
Marcus Delvane
Real Estate Investor
82 Wrenfield Terrace Oakhurst NJ 07155
marcus@quillstonerealtyllc.example
quillstonerealtyllc.example
I have my blog website I would like to add on my car. its called go4renov.example. Also i like clean lines on the business card and other stationery items and keep the color scheme of the logo.
I would like my logo incorporate with a clear and simple design that makes the logo stand out even more.
marcusd418 marcusd418
Hi Everyone, I am liking the designs. I wanted to see if you could include other stationery such as the letter head. I would like to make my final decision seeing the total package. Thank you
I forgot to mention in my brief that I would like to see the different type of finishing option. For example, maybe a matte smooth finish. Something that is not like traditional cards. I'm looking for a premium finish.

```html
<!DOCTYPE html>
<html lang="en">
<head>
<meta charset="utf-8">
<title>Quillstone Realty LLC — Business Card</title>
<link href="https://fonts.googleapis.com/css2?family=Montserrat:wght@400;500;600;700&display=swap" rel="stylesheet">
<style>
  :root {
    --navy: #1f2c4f;
    --navy-deep: #141d36;
    --navy-soft: #2b3b66;
    --green: #8cc63f;
    --green-faint: rgba(140, 198, 63, 0.18);
    --white: #ffffff;
    --stage: #e4e5e8;
    --ink-soft: #d8dceb;
  }
  * { margin: 0; padding: 0; box-sizing: border-box; }
  html, body {
    width: 1200px; height: 901px; overflow: hidden;
    background: var(--stage);
    font-family: "Montserrat", Arial, sans-serif;
  }
  .canvas { position: relative; width: 1200px; height: 901px; }

  .card {
    position: absolute; width: 560px; height: 320px;
    border-radius: 4px; overflow: hidden;
    box-shadow: 0 10px 28px rgba(20, 28, 50, 0.22);
  }

  /* Back of card */
  .card-back { left: 90px; top: 80px; background: var(--navy); }
  .roof-motif {
    position: absolute; inset: 0;
    background:
      radial-gradient(ellipse 170px 120px at 38% 62%, var(--green-faint) 0%, rgba(140,198,63,0) 70%),
      radial-gradient(ellipse 140px 100px at 62% 22%, rgba(140,198,63,0.12) 0%, rgba(140,198,63,0) 70%),
      linear-gradient(125deg, var(--navy) 0%, var(--navy-deep) 30%, var(--navy-soft) 48%, var(--navy-deep) 62%, var(--navy) 82%);
  }
  .back-url {
    position: absolute; right: 26px; bottom: 26px;
    color: var(--ink-soft); font-size: 12px; letter-spacing: 2px; font-weight: 400;
    white-space: nowrap;
  }

  /* Front of card */
  .card-front { left: 540px; top: 440px; background: var(--white); }
  .brand {
    position: absolute; left: 0; right: 0; top: 52px;
    display: flex; justify-content: center; align-items: center; gap: 10px;
  }
  .brand-mark { width: 14px; height: 14px; background: var(--navy); }
  .brand-name { color: var(--navy); font-size: 26px; font-weight: 600; letter-spacing: 0.5px; }
  .accent-line { position: absolute; left: 0; right: 0; top: 148px; height: 3px; background: var(--green); }
  .info-band {
    position: absolute; left: 0; right: 0; top: 158px; bottom: 0; background: var(--navy);
  }
  .person { position: absolute; left: 46px; top: 40px; }
  .person-name { color: var(--green); font-size: 15px; font-weight: 600; }
  .person-title { color: var(--white); font-size: 11px; font-weight: 400; margin-top: 3px; }
  .divider { position: absolute; left: 246px; top: 24px; width: 1px; height: 114px; background: rgba(255,255,255,0.55); }
  .contacts { position: absolute; left: 266px; top: 18px; list-style: none; }
  .contacts li {
    display: flex; align-items: center; gap: 8px;
    color: var(--white); font-size: 10.5px; line-height: 1.25; margin-bottom: 4px;
  }
  .contacts .icon { flex: none; width: 13px; height: 13px; }
  .contacts .address { margin-bottom: 6px; align-items: flex-start; }
</style>
</head>
<body>
<div class="canvas">

  <section class="card card-back">
    <div class="roof-motif" role="img" aria-label="Large overlapping house-roof shapes with small green window accents"></div>
    <span class="back-url">quillstonerealtyllc.example</span>
  </section>

  <section class="card card-front">
    <div class="brand">
      <span class="brand-mark"></span>
      <span class="brand-name">Quillstone Realty LLC</span>
    </div>
    <div class="accent-line"></div>
    <div class="info-band">
      <div class="person">
        <p class="person-name">Marcus Delvane</p>
        <p class="person-title">Real Estate Investor</p>
      </div>
      <div class="divider"></div>
      <ul class="contacts">
        <li class="address">
          <svg class="icon" viewBox="0 0 14 14"><path d="M7 1a4 4 0 0 0-4 4c0 3 4 8 4 8s4-5 4-8a4 4 0 0 0-4-4z" fill="#8cc63f"/><circle cx="7" cy="5" r="1.5" fill="#1f2c4f"/></svg>
          <span>82 Wrenfield Terrace<br>Oakhurst NJ 07155</span>
        </li>
        <li>
          <svg class="icon" viewBox="0 0 14 14"><circle cx="7" cy="7" r="7" fill="#8cc63f"/><path d="M4.5 3.8l1.4-.3.8 1.8-.9.7a5 5 0 0 0 2.2 2.2l.7-.9 1.8.8-.3 1.4C7 9.9 4.1 7 4.5 3.8z" fill="#1f2c4f"/></svg>
          <span>201-555-0147</span>
        </li>
        <li>
          <svg class="icon" viewBox="0 0 14 14"><circle cx="7" cy="7" r="7" fill="#8cc63f"/><rect x="3.5" y="4.5" width="7" height="5" fill="none" stroke="#1f2c4f" stroke-width="1"/><path d="M3.5 4.5L7 7.3l3.5-2.8" fill="none" stroke="#1f2c4f" stroke-width="1"/></svg>
          <span>marcus@quillstonerealtyllc.example</span>
        </li>
        <li>
          <svg class="icon" viewBox="0 0 14 14"><circle cx="7" cy="7" r="7" fill="#8cc63f"/><circle cx="7" cy="7" r="3.6" fill="none" stroke="#1f2c4f" stroke-width="0.9"/><path d="M3.4 7h7.2M7 3.4c-1.5 2-1.5 5.2 0 7.2M7 3.4c1.5 2 1.5 5.2 0 7.2" fill="none" stroke="#1f2c4f" stroke-width="0.8"/></svg>
          <span>go4renov.example</span>
        </li>
        <li>
          <svg class="icon" viewBox="0 0 14 14"><circle cx="7" cy="7" r="7" fill="#8cc63f"/><circle cx="7" cy="7" r="3.6" fill="none" stroke="#1f2c4f" stroke-width="0.9"/><path d="M3.4 7h7.2M7 3.4c-1.5 2-1.5 5.2 0 7.2M7 3.4c1.5 2 1.5 5.2 0 7.2" fill="none" stroke="#1f2c4f" stroke-width="0.8"/></svg>
          <span>quillstonerealtyllc.example</span>
        </li>
      </ul>
    </div>
  </section>

</div>
</body>
</html>
```